We currently have a good logo and we want business cards that can display our logo but also represent our industry - telecom construction - We are a construction company specializing in telecom construction such as installation of fiber optic cable throughout cities and across the country. Nationwide services
We are large enough to handle most any project yet small enough to be a flexible partner and resource.

Target Market(s)

U.S. based telecom carriers and providers

Industry/Entity Type

Construction

Contact Information for Business Card

Business cards should include our logo, phone number and website address. Also, including some information as to our core services would be good.

Colors

Designer to choose colors to be used in the design.

Requirements
Must have
• Colors based on logo
• Must use our logo
• Logo, name, email, website address, phone number
• Tovasco Conduit
• Brent Halvik
• Director of Business Development
• (555) 271-0386
• www.TVSQ-example.com
Nice to have
• Construction services including:
• Small Cell Construction
• Boring/Drilling
• Plowing / Trenching
• Conduit installation
• Fiber pulling
• splicing
• building entries
• Aerial construction
• Aerial Make Ready
• Make Ready Engineering
Should not have
• We are open to ideas

```html
<!DOCTYPE html>
<html lang="en">
<head>
<meta charset="utf-8">
<title>Tovasco Conduit – Business Card</title>
<link href="https://fonts.googleapis.com/css2?family=Montserrat:wght@500;800&display=swap" rel="stylesheet">
<style>
  :root {
    --page-bg: #c4c4c4;
    --card-bg: #000000;
    --card-glow: #3a2a14;
    --brand-blue: #1a7fd6;
    --gold-light: #f6dd8c;
    --gold-mid: #d9aa3a;
    --gold-dark: #a8761c;
    --silver-light: #ffffff;
    --silver-mid: #d6d6d6;
    --silver-dark: #9a9a9a;
    --rule-white: #ffffff;
    --contact-text: #ffffff;
  }
  html, body {
    margin: 0;
    width: 1200px;
    height: 1200px;
    overflow: hidden;
    background: var(--page-bg);
  }
  .canvas { position: relative; width: 1200px; height: 1200px; }
  .card { position: absolute; left: 249px; width: 700px; height: 405px; display: block; }
  .card--gold { top: 135px; }
  .card--silver { top: 652px; }
  .brand-name {
    font-family: 'Montserrat', sans-serif;
    font-weight: 800;
    font-size: 30px;
    fill: var(--brand-blue);
  }
  .contact-text {
    font-family: 'Montserrat', sans-serif;
    font-weight: 500;
    font-size: 13px;
    fill: var(--contact-text);
  }
  .contact-icon-bg { fill: var(--brand-blue); }
  .contact-icon-fill { fill: #ffffff; stroke: none; }
  .contact-icon-line { fill: none; stroke: #ffffff; stroke-width: 1; }
  .contact-icon-cut { fill: none; stroke: var(--brand-blue); stroke-width: 1; }
  .contact-icon-dot { fill: var(--brand-blue); }
</style>
</head>
<body>
<div class="canvas">

  <!-- Gold edition -->
  <svg class="card card--gold" viewBox="0 0 700 405" xmlns="http://www.w3.org/2000/svg">
    <defs>
      <linearGradient id="gold-metal" x1="0" y1="0" x2="1" y2="1">
        <stop offset="0" stop-color="#f6dd8c"/>
        <stop offset="0.5" stop-color="#d9aa3a"/>
        <stop offset="1" stop-color="#a8761c"/>
      </linearGradient>
      <linearGradient id="gold-line" gradientUnits="userSpaceOnUse" x1="100" y1="0" x2="470" y2="0">
        <stop offset="0" stop-color="#d9aa3a"/>
        <stop offset="0.5" stop-color="#f6dd8c"/>
        <stop offset="1" stop-color="#c8962e"/>
      </linearGradient>
      <linearGradient id="card-glow-gold" x1="0" y1="0" x2="1" y2="0">
        <stop offset="0.45" stop-color="#000000"/>
        <stop offset="1" stop-color="#3a2a14"/>
      </linearGradient>
    </defs>
    <rect class="card-base" width="700" height="405" fill="var(--card-bg)"/>
    <rect class="card-glow" width="690" height="255" fill="url(#card-glow-gold)"/>

    <rect class="excavator-art" x="46" y="85" width="110" height="95" fill="url(#gold-metal)" role="img" aria-label="Gold excavator illustration"/>

    <text class="brand-name" x="274" y="88" text-anchor="middle">TOVASCO</text>
    <text class="brand-name" x="274" y="124" text-anchor="middle">CONDUIT</text>

    <g class="conduit-lines" stroke="url(#gold-line)" stroke-width="3" fill="none">
      <line x1="101" y1="175" x2="368" y2="175"/>
      <line x1="101" y1="185" x2="368" y2="185"/>
      <line x1="101" y1="195" x2="368" y2="195"/>
      <path d="M368 185 C420 185, 410 110, 470 100"/>
    </g>

    <rect class="truck-art" x="436" y="80" width="220" height="115" rx="12" fill="url(#gold-metal)" role="img" aria-label="Gold pickup truck carrying a cable reel"/>

    <line class="ground-rule" x1="43" y1="208" x2="663" y2="208" stroke="var(--rule-white)" stroke-width="3"/>

    <g class="contact-list" transform="translate(115 0)">
      <g transform="translate(0 249)"><circle class="contact-icon-bg" r="8"/><path class="contact-icon-fill" d="M-3 -4 L-1 -4 L0 -1 L-1 0 Q0 2 1 2 L2 1 L4 2 L4 4 Q-4 4 -4 -3 Z"/><text class="contact-text" x="16" y="4.5">(555) 271-0386</text></g>
      <g transform="translate(0 277)"><circle class="contact-icon-bg" r="8"/><path class="contact-icon-fill" d="M0 5 L-3.5 -0.5 A4 4 0 1 1 3.5 -0.5 Z"/><circle class="contact-icon-dot" r="1.5" cy="-2"/><text class="contact-text" x="16" y="4.5">1420 Sample Parkway, Springfield, KS 66000</text></g>
      <g transform="translate(0 305)"><circle class="contact-icon-bg" r="8"/><path class="contact-icon-fill" d="M0 -5 L5 0 L3.5 0 L3.5 4 L-3.5 4 L-3.5 0 L-5 0 Z"/><text class="contact-text" x="16" y="4.5">Brent Halvik · Director of Business Development</text></g>
      <g transform="translate(0 334)"><circle class="contact-icon-bg" r="8"/><circle class="contact-icon-line" r="4.5"/><ellipse class="contact-icon-line" rx="2" ry="4.5"/><line class="contact-icon-line" x1="-4.5" x2="4.5"/><text class="contact-text" x="16" y="4.5">www.TVSQ-example.com</text></g>
      <g transform="translate(0 362)"><circle class="contact-icon-bg" r="8"/><rect class="contact-icon-fill" x="-4.5" y="-3" width="9" height="6"/><path class="contact-icon-cut" d="M-4.5 -3 L0 0.5 L4.5 -3"/><text class="contact-text" x="16" y="4.5">brent@TVSQ-example.com</text></g>
    </g>
  </svg>

  <!-- Silver edition -->
  <svg class="card card--silver" viewBox="0 0 700 405" xmlns="http://www.w3.org/2000/svg">
    <defs>
      <linearGradient id="silver-metal" x1="0" y1="0" x2="1" y2="1">
        <stop offset="0" stop-color="#ffffff"/>
        <stop offset="0.5" stop-color="#d6d6d6"/>
        <stop offset="1" stop-color="#9a9a9a"/>
      </linearGradient>
      <linearGradient id="silver-line" gradientUnits="userSpaceOnUse" x1="95" y1="0" x2="475" y2="0">
        <stop offset="0" stop-color="#d6d6d6"/>
        <stop offset="0.5" stop-color="#ffffff"/>
        <stop offset="1" stop-color="#c8c8c8"/>
      </linearGradient>
      <linearGradient id="card-glow-silver" x1="0" y1="0" x2="1" y2="0">
        <stop offset="0.45" stop-color="#000000"/>
        <stop offset="1" stop-color="#3a2a14"/>
      </linearGradient>
    </defs>
    <rect class="card-base" width="700" height="405" fill="var(--card-bg)"/>
    <rect class="card-glow" width="690" height="255" fill="url(#card-glow-silver)"/>

    <rect class="excavator-art" x="39" y="78" width="113" height="100" fill="url(#silver-metal)" role="img" aria-label="Silver excavator illustration"/>

    <text class="brand-name" x="270" y="82" text-anchor="middle">TOVASCO</text>
    <text class="brand-name" x="270" y="118" text-anchor="middle">CONDUIT</text>

    <g class="conduit-lines" stroke="url(#silver-line)" stroke-width="3" fill="none">
      <line x1="95" y1="166" x2="368" y2="166"/>
      <line x1="95" y1="177" x2="368" y2="177"/>
      <line x1="95" y1="188" x2="368" y2="188"/>
      <path d="M368 177 C425 177, 410 100, 475 93"/>
    </g>

    <rect class="truck-art" x="438" y="70" width="222" height="120" rx="12" fill="url(#silver-metal)" role="img" aria-label="Silver pickup truck carrying a cable reel"/>

    <line class="ground-rule" x1="36" y1="202" x2="671" y2="202" stroke="var(--rule-white)" stroke-width="3"/>

    <g class="contact-list" transform="translate(110 0)">
      <g transform="translate(0 243)"><circle class="contact-icon-bg" r="8"/><path class="contact-icon-fill" d="M-3 -4 L-1 -4 L0 -1 L-1 0 Q0 2 1 2 L2 1 L4 2 L4 4 Q-4 4 -4 -3 Z"/><text class="contact-text" x="16" y="4.5">(555) 271-0386</text></g>
      <g transform="translate(0 272)"><circle class="contact-icon-bg" r="8"/><path class="contact-icon-fill" d="M0 5 L-3.5 -0.5 A4 4 0 1 1 3.5 -0.5 Z"/><circle class="contact-icon-dot" r="1.5" cy="-2"/><text class="contact-text" x="16" y="4.5">1420 Sample Parkway, Springfield, KS 66000</text></g>
      <g transform="translate(0 300)"><circle class="contact-icon-bg" r="8"/><path class="contact-icon-fill" d="M0 -5 L5 0 L3.5 0 L3.5 4 L-3.5 4 L-3.5 0 L-5 0 Z"/><text class="contact-text" x="16" y="4.5">Brent Halvik · Director of Business Development</text></g>
      <g transform="translate(0 329)"><circle class="contact-icon-bg" r="8"/><circle class="contact-icon-line" r="4.5"/><ellipse class="contact-icon-line" rx="2" ry="4.5"/><line class="contact-icon-line" x1="-4.5" x2="4.5"/><text class="contact-text" x="16" y="4.5">www.TVSQ-example.com</text></g>
      <g transform="translate(0 358)"><circle class="contact-icon-bg" r="8"/><rect class="contact-icon-fill" x="-4.5" y="-3" width="9" height="6"/><path class="contact-icon-cut" d="M-4.5 -3 L0 0.5 L4.5 -3"/><text class="contact-text" x="16" y="4.5">brent@TVSQ-example.com</text></g>
    </g>
  </svg>

</div>
</body>
</html>
```